New name flyer

We have just changed our business name from kR Property group to Harbour Lantern. We want to distribute a flyer to the local community to inform them of the change. We are a realestate agency which focuses mainly on property management but also sales. We service from Brisbane to the Sunshine coast.

Target Market(s)

Local community

Industry/Entity Type

realestate

Requirements
Must have
• Details of name change
Nice to have
• Servicing area Brisbane and Sunshine Coast, no change in management or services we offer, and will continue pride ourselves on offering a high level of service, with the same team from the Gold to Sunshine Coast.
Should not have
• too much wording.

```html
<!DOCTYPE html>
<html lang="en">
<head>
<meta charset="utf-8">
<title>New Name Flyer – Harbour Lantern</title>
<link rel="stylesheet" href="https://fonts.googleapis.com/css2?family=Poppins:wght@300;400;600;800&display=swap">
<style>
  :root {
    --backdrop: #e3e3e3;
    --navy: #2f3a86;
    --navy-deep: #263077;
    --gold: #e5a92e;
    --white: #ffffff;
    --paper: #f4f5f7;
    --brand-blue: #2a6fb8;
    --curl-light: #c5c8dc;
    --curl-dark: #5b5f86;
    --room-light: #f1ebe1;
    --room-mid: #d9ccb7;
    --room-dark: #a08b70;
  }
  * { margin: 0; padding: 0; box-sizing: border-box; }
  html, body {
    width: 1200px; height: 900px; overflow: hidden;
    background: var(--backdrop);
    font-family: "Poppins", sans-serif;
  }
  .flyer {
    position: absolute; left: 100px; top: 100px;
    width: 1000px; height: 700px;
    background: var(--navy);
    overflow: hidden;
    box-shadow: 0 14px 40px rgba(0,0,0,0.18);
  }
  .flyer-art { position: absolute; inset: 0; }
  .old-name {
    position: absolute; left: 24px; top: 46px;
    font-weight: 600; font-size: 16px; line-height: 1.2;
    color: var(--brand-blue); white-space: nowrap;
  }
  .headline {
    position: absolute; left: 470px; top: 48px;
    font-weight: 800; line-height: 1.02; letter-spacing: -0.5px;
  }
  .headline .line-gold { display: block; color: var(--gold); font-size: 52px; }
  .headline .line-white { display: block; color: var(--white); font-size: 56px; }
  .change-note {
    position: absolute; left: 474px; top: 232px;
    font-weight: 300; font-size: 15px; color: var(--gold);
  }
  .new-name {
    position: absolute; left: 560px; top: 280px;
    font-weight: 600; font-size: 44px; color: var(--white);
    letter-spacing: 1px;
  }
  .service-area {
    position: absolute; left: 190px; top: 330px;
    display: flex; gap: 10px; color: var(--white);
    font-size: 19px; line-height: 1.22;
  }
  .service-area .pin { width: 16px; height: 22px; margin-top: 3px; flex: none; }
  .service-area .light { font-weight: 300; }
  .service-area strong { font-weight: 800; }
</style>
</head>
<body>
  <main class="flyer">
    <svg class="flyer-art" viewBox="0 0 1000 700" width="1000" height="700">
      <defs>
        <linearGradient id="curlShade" x1="0" y1="0" x2="1" y2="0.3">
          <stop offset="0" stop-color="var(--curl-dark)"/>
          <stop offset="0.55" stop-color="var(--curl-light)"/>
          <stop offset="1" stop-color="var(--curl-dark)"/>
        </linearGradient>
        <linearGradient id="roomTone" x1="0" y1="0" x2="1" y2="1">
          <stop offset="0" stop-color="var(--room-light)"/>
          <stop offset="0.6" stop-color="var(--room-mid)"/>
          <stop offset="1" stop-color="var(--room-dark)"/>
        </linearGradient>
      </defs>
      <rect class="panel-navy" width="1000" height="700" fill="var(--navy)"/>
      <polygon class="corner-paper" points="0,0 300,0 0,450" fill="var(--paper)"/>
      <path class="page-curl" d="M300,0 C262,40 222,110 180,180 C130,265 70,360 0,450 C40,360 80,270 130,190 C180,110 230,50 262,0 Z" fill="url(#curlShade)"/>
      <path class="photo-interior" role="img" aria-label="Photo of a bright living room with armchairs, teal cushions and large windows"
            d="M0,500 C250,500 560,420 1000,355 L1000,700 L0,700 Z" fill="url(#roomTone)"/>
      <path class="wave-band" d="M0,492 C250,492 560,410 1000,345" fill="none" stroke="var(--white)" stroke-width="18"/>
    </svg>

    <div class="old-name">kR Property group</div>

    <h1 class="headline">
      <span class="line-gold">just changed our</span>
      <span class="line-white">business name !</span>
    </h1>
    <p class="change-note">from kR Property group to Harbour Lantern</p>
    <div class="new-name">Harbour Lantern</div>

    <div class="service-area">
      <svg class="pin" viewBox="0 0 16 22"><path d="M8 1a7 7 0 0 0-7 7c0 5 7 13 7 13s7-8 7-13a7 7 0 0 0-7-7z" fill="var(--gold)"/><circle cx="8" cy="8" r="2.6" fill="var(--navy)"/></svg>
      <p><span class="light">We service from</span><br><strong>Brisbane</strong><br><span class="light">to the</span><br><strong>Sunshine coast</strong></p>
    </div>
  </main>
</body>
</html>
```